Business Card Design for Cybersecurity Company - Quorvent Systems

We need a business card design for our new cybersecurity company, Quorvent. We’re going for a clean, hi tech look that feels modern, premium, and trustworthy. We want a design that really stands out and makes people say WOW when we hand it over!

Quorvent delivers reliable IT support and managed services for small and mid sized businesses. We help companies stay secure, efficient, and connected through proactive monitoring, cybersecurity services, cloud management, and remote support.

Target Market(s)

Designers should target small and mid sized businesses that need dependable cybersecurity and IT support.

Industry/Entity Type

Cybersecurity, Managed Service Provider, IT services

Contact Information for Business Card

Contact information

Requirements
Must have
• The card should look clean, modern, and tech focused, with the Quorvent logo, clear contact info, and strong readability. It needs to feel premium and professional while still keeping a simple layout that fits a cybersecurity and IT brand.
Nice to have
• Nice to have elements include subtle touches that give the card a modern, tech feel, along with a layout that works well in different background styles.
Should not have
• The card should avoid clutter, loud graphics, or anything that takes attention away from the logo and contact details.

```html
<!DOCTYPE html>
<html lang="en">
<head>
<meta charset="utf-8">
<title>Quorvent Systems – Business Card</title>
<link href="https://fonts.googleapis.com/css2?family=Poppins:wght@400;500;600;700&display=swap" rel="stylesheet">
<style>
  :root {
    --stage: #1c1c20;
    --blue: #4a6bb5;
    --violet: #6a4aa2;
    --ink: #141414;
    --brand: #5450b0;
    --white: #ffffff;
  }
  html, body {
    margin: 0;
    width: 1200px;
    height: 1200px;
    overflow: hidden;
    background: var(--stage);
    font-family: "Poppins", sans-serif;
  }
  .sheet {
    position: relative;
    width: 1200px;
    height: 1200px;
  }
  .card {
    position: absolute;
    left: 150px;
    width: 900px;
    height: 514px;
    overflow: hidden;
    box-shadow: 0 14px 40px rgba(0,0,0,0.5);
  }
  .card--back {
    top: 61px;
    background: linear-gradient(100deg, var(--blue) 0%, #5a5fae 45%, var(--violet) 100%);
  }
  .card--front {
    top: 625px;
    background: var(--white);
  }
  .back-decor {
    position: absolute;
    right: 0;
    top: 0;
    width: 330px;
    height: 100%;
    background: linear-gradient(90deg, rgba(255,255,255,0) 0%, rgba(255,255,255,0.08) 40%, rgba(255,255,255,0.12) 100%);
  }
  .brand {
    position: absolute;
    display: flex;
    align-items: center;
    gap: 18px;
    font-weight: 600;
    white-space: nowrap;
  }
  .brand__dot {
    border-radius: 50%;
    flex: none;
  }
  .card--back .brand {
    left: 150px;
    top: 205px;
    font-size: 54px;
    color: var(--white);
  }
  .card--back .brand__dot {
    width: 70px;
    height: 70px;
    border: 4px solid var(--white);
    box-sizing: border-box;
  }
  .front-shape {
    position: absolute;
    inset: 0;
  }
  .card--front .brand {
    left: 70px;
    top: 70px;
    font-size: 48px;
    color: var(--brand);
  }
  .card--front .brand__dot {
    width: 64px;
    height: 64px;
    border: 4px solid var(--brand);
    box-sizing: border-box;
  }
  .person {
    position: absolute;
    left: 70px;
    top: 205px;
  }
  .person__name {
    margin: 0;
    font-size: 34px;
    font-weight: 700;
    letter-spacing: 0.5px;
    color: var(--brand);
    line-height: 1.1;
  }
  .person__role {
    margin: 4px 0 0;
    font-size: 20px;
    font-weight: 500;
    color: var(--ink);
  }
  .contacts {
    position: absolute;
    left: 70px;
    top: 320px;
    margin: 0;
    padding: 0;
    list-style: none;
  }
  .contacts__item {
    display: flex;
    align-items: center;
    gap: 14px;
    height: 42px;
    font-size: 27px;
    font-weight: 500;
    color: var(--ink);
  }
  .contacts__icon {
    width: 30px;
    height: 30px;
    flex: none;
  }
</style>
</head>
<body>
<main class="sheet">

  <section class="card card--back" aria-label="Card back">
    <div class="back-decor" role="img" aria-label="Faint circuit-trace decoration"></div>
    <div class="brand">
      <span class="brand__dot"></span>
      <span class="brand__name">Quorvent Systems</span>
    </div>
  </section>

  <section class="card card--front" aria-label="Card front">
    <svg class="front-shape" viewBox="0 0 900 514" preserveAspectRatio="none" aria-hidden="true">
      <defs>
        <linearGradient id="front-band" x1="0" y1="0" x2="1" y2="1">
          <stop offset="0" stop-color="#4f63b2"/>
          <stop offset="1" stop-color="#6b49a0"/>
        </linearGradient>
      </defs>
      <rect width="900" height="514" fill="url(#front-band)"/>
      <path d="M0 0 H330 C600 10 800 170 785 330 C775 440 690 500 590 514 H0 Z" fill="#ffffff"/>
      <path d="M330 0 C575 14 765 170 752 325 C742 430 665 492 575 514" fill="none" stroke="#6a4aa2" stroke-width="12"/>
      <path d="M330 0 C575 14 765 170 752 325 C742 430 665 492 575 514" fill="none" stroke="#ffffff" stroke-width="3" transform="translate(26 4)"/>
    </svg>

    <div class="brand">
      <span class="brand__dot"></span>
      <span class="brand__name">Quorvent Systems</span>
    </div>

    <div class="person">
      <h1 class="person__name">DANA MERCER</h1>
      <p class="person__role">Owner | CEO | Quorvent Systems</p>
    </div>

    <ul class="contacts">
      <li class="contacts__item">
        <svg class="contacts__icon" viewBox="0 0 30 30" aria-hidden="true"><circle cx="15" cy="15" r="15" fill="#5a55b0"/><path d="M10 8 l3 0 l1.5 4 l-2 1.5 a9 9 0 0 0 4 4 l1.5-2 l4 1.5 l0 3 a2 2 0 0 1-2 2 a14 14 0 0 1-12-12 a2 2 0 0 1 2-2z" fill="#fff"/></svg>
        <span>(855) 555-0148</span>
      </li>
      <li class="contacts__item">
        <svg class="contacts__icon" viewBox="0 0 30 30" aria-hidden="true"><circle cx="15" cy="15" r="15" fill="#5a55b0"/><rect x="10.5" y="7" width="9" height="16" rx="1.5" fill="none" stroke="#fff" stroke-width="1.8"/><circle cx="15" cy="20" r="1" fill="#fff"/></svg>
        <span>(813) 555-0172</span>
      </li>
      <li class="contacts__item">
        <svg class="contacts__icon" viewBox="0 0 30 30" aria-hidden="true"><circle cx="15" cy="15" r="15" fill="#5a55b0"/><rect x="8" y="10" width="14" height="10" fill="none" stroke="#fff" stroke-width="1.8"/><path d="M8 10 l7 6 l7-6" fill="none" stroke="#fff" stroke-width="1.8"/></svg>
        <span>dana@quorvent.com</span>
      </li>
      <li class="contacts__item">
        <svg class="contacts__icon" viewBox="0 0 30 30" aria-hidden="true"><circle cx="15" cy="15" r="15" fill="#5a55b0"/><circle cx="15" cy="15" r="7.5" fill="none" stroke="#fff" stroke-width="1.6"/><ellipse cx="15" cy="15" rx="3.2" ry="7.5" fill="none" stroke="#fff" stroke-width="1.4"/><path d="M7.5 15 h15" stroke="#fff" stroke-width="1.4"/></svg>
        <span>quorvent.com</span>
      </li>
    </ul>
  </section>

</main>
</body>
</html>
```